Frischer, moderner, emotionaler Baumarkt-Onlineshop sucht passende Außendarstellung
Zielgruppe
Wir sind gerade im Aufbau eines Onlinebaumarktes. In diesem Baumarkt bekommt man vom Nagel bis hin zum neuen Fußboden alles was das Herz begehrt. Wir möchten der Begleiter für jeden Heimwerker sein, der eine gute Beratung, hochwertige Produkte und einen aufgeräumten Fachhandel sucht. Wir wollen einen emotionalen Onlineshop schaffen, bei dem das richtige Produkt dich sucht und nicht du stundenlang das richtige Produkt.
Aufgabenstellung
Wir möchten ein modernes und frisches Bild, der etwas eingestaubten Baumarktlandschaft vermitteln. Bei uns soll es Spaß machen, nach tollen Produkten zu stöbern. Der Kunde soll visuell angesprochen werden und sich intuitiv auf unseren Seiten bewegen können. Wenn man sich die gängigen Shopseiten anschaut, hat man eine ewig lange Navigation um zu seinem Produkt zu kommen. Wir möchten diesen Prozess, durch intelligente Filter gerne verkürzen, so dass jeder Laie sein Produkt ganz leicht findet.
Die Farben der Seite sollten sich an das Logo anlehnen oder diese auch einfließen lassen, damit die Seite wie aus einem Guss wirkt. Interessieren würde uns auch wie die Seite nicht nur auf dem Desktop aussieht, sondern auch seine Übersichtigkeit auf einem Tablet oder Smartphone beibehält.

```html
<!DOCTYPE html>
<html lang="de">
<head>
<meta charset="utf-8">
<title>werkhof-online.de – Startseite Tablet & Smartphone</title>
<link rel="stylesheet" href="https://fonts.googleapis.com/css2?family=Arimo:wght@400;700&family=Roboto+Condensed:wght@700&display=swap">
<style>
:root{
  --green:#84b81c;
  --green-dark:#6f9c14;
  --blue:#1b3a8f;
  --orange:#e8631a;
  --white:#ffffff;
  --ink:#1e1e1e;
  --grey:#9a9a9a;
  --line:#d9d9d9;
  --stage:#f2f2f2;
}
*{box-sizing:border-box;margin:0;padding:0}
html,body{width:1200px;height:969px;overflow:hidden;background:var(--stage);font-family:"Arimo",Arial,sans-serif;color:var(--ink)}
h2{font-weight:400;white-space:nowrap}
.screen{position:absolute;background:var(--white);overflow:hidden;box-shadow:0 2px 14px rgba(0,0,0,.12)}
.screen--tablet{left:30px;top:33px;width:677px;height:902px}
.screen--phone{left:770px;top:125px;width:404px;height:718px}
.abs{position:absolute}

/* header */
.brand{position:absolute;font-family:"Roboto Condensed",Arial,sans-serif;font-weight:700;color:var(--blue);line-height:1}
.brand__mark{display:inline-block;background:var(--blue);vertical-align:middle;margin-right:8px}
.topnav{position:absolute;display:flex;border:1px solid var(--line);border-top:none;font-size:11px;font-weight:700}
.topnav span{padding:5px 8px;border-right:1px solid var(--line)}
.topnav span:last-child{border-right:none}
.topnav .muted{color:var(--grey);font-weight:400}
.field{position:absolute;border:1px solid var(--line);font-size:9px;color:var(--grey);padding:3px 6px;display:flex;justify-content:space-between;align-items:center}
.cart-label{position:absolute;font-size:11px;font-weight:700}
.cart-sum{position:absolute;font-size:9px;color:var(--orange)}

/* sections */
.panel{position:absolute;background:var(--green)}
.panel__title{position:absolute;color:var(--white);font-weight:400;z-index:2;line-height:1.1}
.tag{position:absolute;z-index:3;background:var(--blue);color:var(--white);line-height:1;border:1px solid #2d50b0}
.art{position:absolute;z-index:1}
.art--house{background:radial-gradient(ellipse at 55% 55%,#f5f5f2 0%,#e4e2dc 38%,#b9b09a 58%,var(--green) 75%)}
.art--pool{background:linear-gradient(180deg,#9aa48a 0%,#b5c0c4 30%,#5fa9d6 45%,#a9a39a 65%,#a08a78 100%);opacity:.85}
.art--heater{background:radial-gradient(circle at 50% 50%,#555 0%,#222 55%,#fff 72%)}
.art--mixer{background:radial-gradient(circle at 45% 40%,#f39a3a 0%,#e8771c 40%,#fff 70%)}

/* offers */
.offers-title{position:absolute;font-size:23px;font-weight:400;z-index:2}
.price{position:absolute;color:var(--orange);font-weight:700;font-family:"Roboto Condensed",Arial,sans-serif;z-index:2}
.price sup{font-size:.5em}
.price-old{position:absolute;color:var(--orange);font-size:7px;font-weight:700;text-decoration:line-through;z-index:2}
.tax{position:absolute;font-size:5px}
.btn{position:absolute;background:var(--green);color:var(--white);font-size:6px;padding:2px 4px;display:flex;justify-content:space-between}

/* brands */
.brands-title{position:absolute;color:var(--white);font-size:22px;font-weight:400}
.brand-chip{position:absolute;background:var(--white);color:var(--blue);font-weight:700;font-size:11px;display:flex;align-items:center;justify-content:center}
.menu-bar{position:absolute;background:var(--blue);height:4px;width:40px}
</style>
</head>
<body>

<!-- Tablet -->
<main class="screen screen--tablet">
  <header>
    <div class="brand" style="left:24px;top:34px;font-size:38px"><span class="brand__mark" style="width:10px;height:10px"></span>werkhof</div>
    <div class="brand" style="left:100px;top:80px;font-size:17px">-online.de</div>
    <nav class="topnav" style="left:312px;top:0"><span>👤 Mein Konto</span><span>Merkzettel</span><span>Service/Hilfe ⌄</span><span>EUR <b class="muted">USD</b></span></nav>
    <div class="field" style="left:255px;top:66px;width:194px;height:18px"><span>Suche:</span><span>⌕</span></div>
    <div class="cart-label" style="left:458px;top:48px">WARENKORB</div>
    <div class="cart-sum" style="left:578px;top:48px">0,00 €*</div>
    <div class="field" style="left:458px;top:66px;width:148px;height:18px"><span>Positionen anzeigen</span><span>⌄</span></div>
    <svg class="abs" style="left:620px;top:38px" width="48" height="56" viewBox="0 0 48 56" aria-hidden="true"><g fill="none" stroke="#555" stroke-width="2"><path d="M6 2v40h36M14 2v40M30 2v40"/><rect x="4" y="40" width="40" height="5"/><circle cx="10" cy="50" r="4"/><circle cx="38" cy="50" r="4"/></g></svg>
  </header>

  <section class="panel" style="left:0;top:108px;width:677px;height:378px">
    <h2 class="panel__title" style="left:28px;top:12px;font-size:28px">1. Kategorie wählen</h2>
    <div class="art art--house" role="img" aria-label="Illustration: aufgeschnittenes Einfamilienhaus mit Garten und Baum" style="left:45px;top:48px;width:590px;height:330px"></div>
    <div class="tag" style="left:514px;top:24px;width:138px;height:80px;font-size:29px;padding:10px 16px">Garten/<br>Außen</div>
  </section>

  <section class="panel" style="left:0;top:498px;width:677px;height:222px">
    <h2 class="panel__title" style="left:20px;top:4px;font-size:22px">2. Unterkategorie</h2>
    <div class="art art--pool" role="img" aria-label="Foto: Pool mit Holzdeck und Liegestühlen im Garten" style="left:120px;top:16px;width:410px;height:196px"></div>
    <div class="tag" style="left:514px;top:14px;width:138px;height:80px;font-size:29px;padding:12px 16px">Pool/<br>Teich</div>
  </section>

  <section class="abs" style="left:0;top:720px;width:330px;height:182px">
    <h2 class="offers-title" style="left:35px;top:20px">Wochenangebote</h2>
    <div class="art art--heater" role="img" aria-label="Produktfoto: Heizlüfter" style="left:38px;top:68px;width:80px;height:80px"></div>
    <div class="art art--mixer" role="img" aria-label="Produktfoto: Betonmischer" style="left:240px;top:24px;width:76px;height:90px"></div>
    <div class="price" style="left:130px;top:76px;font-size:18px">189,<sup>00</sup> €</div>
    <div class="tax" style="left:130px;top:108px">inkl. gesetzl. MwSt.</div>
    <div class="btn" style="left:130px;top:122px;width:94px"><span>Zum Angebot</span><span>›</span></div>
    <div class="price-old" style="left:242px;top:128px">159,00 €</div>
    <div class="price" style="left:242px;top:136px;font-size:18px">139,<sup>00</sup> €</div>
  </section>

  <section class="panel" style="left:330px;top:732px;width:347px;height:170px">
    <h2 class="brands-title" style="left:84px;top:18px">Marken zum Thema</h2>
    <div class="brand-chip" style="left:82px;top:56px;width:44px;height:42px">Fornax</div>
    <div class="brand-chip" style="left:136px;top:56px;width:84px;height:40px">Aquavo</div>
    <div class="brand-chip" style="left:230px;top:58px;width:70px;height:36px">Wolkig</div>
    <div class="brand-chip" style="left:82px;top:116px;width:84px;height:22px">Rendo</div>
    <div class="brand-chip" style="left:190px;top:116px;width:104px;height:22px">Lindal</div>
  </section>
</main>

<!-- Smartphone -->
<main class="screen screen--phone">
  <header>
    <div class="brand" style="left:18px;top:22px;font-size:26px"><span class="brand__mark" style="width:7px;height:7px;margin-right:5px"></span>werkhof</div>
    <div class="brand" style="left:62px;top:52px;font-size:11px">-online.de</div>
    <div class="cart-label" style="left:192px;top:32px;font-size:6px">WARENKORB</div>
    <div class="cart-sum" style="left:262px;top:32px;font-size:5px">0,00 €*</div>
    <div class="field" style="left:192px;top:43px;width:84px;height:10px;font-size:5px;padding:1px 3px"><span>Positionen anzeigen</span><span>⌄</span></div>
    <svg class="abs" style="left:286px;top:26px" width="30" height="34" viewBox="0 0 48 56" aria-hidden="true"><g fill="none" stroke="#555" stroke-width="2.5"><path d="M6 2v40h36M14 2v40M30 2v40"/><rect x="4" y="40" width="40" height="5"/><circle cx="10" cy="50" r="4"/><circle cx="38" cy="50" r="4"/></g></svg>
    <div class="menu-bar" style="left:346px;top:24px"></div>
    <div class="menu-bar" style="left:346px;top:34px"></div>
    <div class="menu-bar" style="left:346px;top:44px"></div>
  </header>

  <section class="panel" style="left:4px;top:70px;width:396px;height:293px">
    <h2 class="panel__title" style="left:16px;top:6px;font-size:16px">1. Kategorie wählen</h2>
    <div class="art art--house" role="img" aria-label="Illustration: aufgeschnittenes Einfamilienhaus mit Garten und Baum" style="left:14px;top:40px;width:380px;height:250px"></div>
    <div class="tag" style="left:302px;top:13px;width:80px;height:47px;font-size:16px;padding:7px 8px">Garten/<br>Außen</div>
  </section>

  <section class="panel" style="left:4px;top:371px;width:396px;height:183px">
    <h2 class="panel__title" style="left:12px;top:6px;font-size:13px">2. Unterkategorie</h2>
    <div class="art art--pool" role="img" aria-label="Foto: Pool mit Holzdeck und Liegestühlen im Garten" style="left:70px;top:30px;width:242px;height:138px"></div>
    <div class="tag" style="left:302px;top:15px;width:80px;height:45px;font-size:16px;padding:5px 8px">Pool/<br>Teich</div>
  </section>

  <section class="abs" style="left:0;top:554px;width:404px;height:164px">
    <h2 class="offers-title" style="left:8px;top:5px;font-size:20px">Wochenangebote</h2>
    <div class="art art--heater" role="img" aria-label="Produktfoto: Heizlüfter" style="left:32px;top:40px;width:84px;height:84px"></div>
    <div class="art art--mixer" role="img" aria-label="Produktfoto: Betonmischer" style="left:284px;top:2px;width:90px;height:96px"></div>
    <div class="price" style="left:134px;top:52px;font-size:18px">189,<sup>00</sup> €</div>
    <div class="tax" style="left:134px;top:84px">inkl. gesetzl. MwSt.</div>
    <div class="btn" style="left:134px;top:98px;width:90px"><span>Zum Angebot</span><span>›</span></div>
    <div class="price-old" style="left:252px;top:98px">159,00 €</div>
    <div class="price" style="left:252px;top:106px;font-size:19px">139,<sup>00</sup> €</div>
  </section>
</main>

</body>
</html>
```